Talking Ledger Hour Podcast artwork

Podcast Artwork. Hosted by Marla Oskevich. Also looking for a clear and distinct font that can be used as a logo for business cards and website. This podcast is a long format, conversation driven podcast about the stories behind cryptocurrencies and blockchain technology. We dive into what's exciting and what's to come and how industries, the internet, and the way we do business is being changed through this new technology. It will be conversation driven rather than tech heavy. Navy or Royal Blue and Hot Pink would be our first choices of colours.

Target Market(s)

Finance, Entertainment, Technology sectors.

Contact Information for Business Card

Marla Oskevich
Podcast Host
@talkingledger
talkingledgerhour.example
talkingledger@mailbox.example

Logo Text

Talking Ledger Hour Podcast

Font styles to use
Sans Serif

Colors
0455a3
e667a6

Requirements
Must have
• Colours that match the website: talkingledgerhour.example
Nice to have
• A style that matches the website talking ledger hour.com

```html
<!DOCTYPE html>
<html lang="en">
<head>
<meta charset="utf-8">
<title>Talking Ledger Hour Podcast Artwork</title>
<link rel="stylesheet" href="https://fonts.googleapis.com/css2?family=Poppins:wght@300;700&display=swap">
<style>
  :root {
    --brand-blue: #0455a3;
    --brand-pink: #e667a6;
    --paper: #ffffff;
    --host-grey: #4a4852;
  }
  html, body {
    margin: 0;
    padding: 0;
    width: 1200px;
    height: 1200px;
    overflow: hidden;
    background: var(--paper);
  }
  .artwork {
    position: relative;
    width: 1200px;
    height: 1200px;
    background: var(--paper);
    font-family: "Poppins", sans-serif;
  }
  .frame {
    position: absolute;
    left: 100px;
    top: 98px;
    width: 970px;
    height: 968px;
    box-sizing: border-box;
    border: 26px solid var(--brand-pink);
  }
  .corner-block {
    position: absolute;
    left: 62px;
    top: 62px;
    width: 182px;
    height: 182px;
    background: var(--brand-blue);
  }
  .brand-dot {
    position: absolute;
    left: 536px;
    top: 420px;
    width: 130px;
    height: 130px;
    border-radius: 50%;
    background: var(--brand-blue);
  }
  .title-block {
    position: absolute;
    right: 332px;
    top: 580px;
    text-align: right;
  }
  .show-name {
    margin: 0;
    color: var(--brand-blue);
    font-weight: 700;
    font-size: 74px;
    line-height: 86px;
    letter-spacing: -1px;
  }
  .show-name span {
    display: block;
  }
  .host-name {
    margin: 14px 0 0;
    color: var(--host-grey);
    font-weight: 300;
    font-size: 37px;
    line-height: 44px;
    letter-spacing: 1px;
  }
</style>
</head>
<body>
  <main class="artwork">
    <div class="frame"></div>
    <div class="corner-block"></div>
    <div class="brand-dot"></div>
    <div class="title-block">
      <h1 class="show-name"><span>Talking Ledger</span><span>Hour</span></h1>
      <p class="host-name">Marla Oskevich</p>
    </div>
  </main>
</body>
</html>
```